passmarlo.com

Develop a website for passmarlo.com will be a site to sell tickets for concerts, shows, shows, theaters and others. I need a web design easy view, very easy to use and accumulate events by date. The aim is to develop the site was connected to a complex system that is already developed. (Important this page to a robust system was connected via links the idea is to develop only the front view)
Updates

Reason: I need more designs yet we have not made the decision

Target Market(s)

millennials, adults, who want to enjoy concerts and shows

Industry/Entity Type

Event

Number of Pages Required

5+ page

Colors
1b1b1b
aaaaaa
ffffff

Requirements
Must have
• Easy Vista, accumulation of upcoming events, past events. The tabs should have are: 1 Start: In this part of upcoming events occur. You could put a banner on the top and down the events by date. 2. How to order: page with instructions on how to purchase tickets 3. About Us: The company history 4. Contact: Phones and template for contact by mail 5. Our policies: shopping 6. Notice Privacy: Privacy Notice Copoy 7. Centers Sale: physical places where they can purchase tickets Promoters 8. access: Link to a template
Nice to have
• as you can see p www.fondarivent.com or entravú.com or pasuqo.com or gatelorvi.com (important this page to a robust system was connected via links the idea is to develop only the front view)
Should not have
• Many things Tangled

```html
<!DOCTYPE html>
<html lang="en">
<head>
<meta charset="utf-8">
<title>passmarlo.com — Tickets for concerts and shows</title>
<link rel="stylesheet" href="https://fonts.googleapis.com/css2?family=Open+Sans:wght@400;600&family=Montserrat:wght@700;800&display=swap">
<style>
:root{
  --ink:#1b1b1b;
  --night:#1a0a12;
  --wine:#2a0c18;
  --grey:#aaaaaa;
  --white:#ffffff;
  --red:#e04a4a;
  --red-dark:#b93333;
  --bar:#141214;
  --footer:#100c0e;
}
*{box-sizing:border-box;margin:0;padding:0}
html,body{width:783px;height:1200px;overflow:hidden;background:var(--night)}
body{font-family:"Open Sans",Arial,sans-serif;color:var(--white);position:relative}
.page{position:relative;width:783px;height:1200px;overflow:hidden}

/* header */
.topbar{position:absolute;left:0;top:0;width:783px;height:73px;background:linear-gradient(90deg,#1d0a14,#2c0e1c 50%,#1d0a14)}
.phone{position:absolute;left:68px;top:22px;display:flex;align-items:center;gap:9px;font-size:14.5px}
.phone-icon{width:28px;height:28px;border:1.5px solid var(--white);border-radius:50%;display:flex;align-items:center;justify-content:center}
.brand{position:absolute;left:343px;top:13px;width:97px;height:48px;background:var(--red);border-radius:4px;display:flex;align-items:center;justify-content:center;font-family:"Montserrat",sans-serif;font-weight:700;font-size:13px;letter-spacing:.5px;color:var(--white)}
.social{position:absolute;display:flex;gap:8px}
.social span{display:block;width:15px;height:15px;border-radius:2px}
.social.top{left:628px;top:28px}
.social.top span:nth-child(1){background:#3b6fd1}
.social.top span:nth-child(2){background:#2ea6e6}
.social.top span:nth-child(3){background:#2a7ab8}
.social.top span:nth-child(4){background:#d6453a}

/* nav */
.nav{position:absolute;left:0;top:73px;width:783px;height:38px;background:var(--bar);display:flex;padding-left:58px}
.nav a{display:block;height:38px;line-height:38px;font-size:11px;color:var(--white);text-decoration:none;padding:0 16px;white-space:nowrap}
.nav a.active{background:#0a0a0a;border-top:2px solid var(--red);line-height:34px;padding:0 21px}

/* hero */
.hero{position:absolute;left:0;top:111px;width:783px;height:321px;background:
  radial-gradient(ellipse 40% 55% at 50% 40%,rgba(120,60,70,.55),transparent 70%),
  linear-gradient(180deg,#3a1018 0%,#4a141c 45%,#2b0c12 72%,#5a3a2c 86%,#231510 100%)}
.hero-title{position:absolute;left:0;width:783px;top:113px;text-align:center;font-family:"Montserrat",sans-serif;font-weight:800;font-size:40px;letter-spacing:.5px;line-height:1}
.hero-sub{position:absolute;left:0;width:783px;top:155px;text-align:center;font-size:21px;font-weight:400;line-height:1}
.hero-arrows{position:absolute;left:684px;top:285px;display:flex;gap:5px}
.hero-arrows span{width:18px;height:18px;border-radius:50%;background:rgba(0,0,0,.55);display:flex;align-items:center;justify-content:center}

/* events */
.events{position:absolute;left:0;top:432px;width:783px;height:578px;background:linear-gradient(180deg,#1c0810,#2a0b18 50%,#1e0a12)}
.events h2{position:absolute;left:0;width:783px;top:38px;text-align:center;font-size:19px;font-weight:600;letter-spacing:.5px}
.event{position:absolute;width:217px;height:203px;overflow:hidden}
.event .photo{position:absolute;inset:0}
.caption{position:absolute;left:0;bottom:0;width:100%;height:47px;background:rgba(20,14,18,.78)}
.date{position:absolute;left:0;top:0;width:35px;height:47px;background:var(--red);text-align:center;font-size:8.5px;line-height:11.5px;padding-top:6px}
.caption h3{position:absolute;left:42px;top:12px;font-size:10.5px;font-weight:600;letter-spacing:.2px}
.caption p{position:absolute;left:42px;top:27px;font-size:8px;color:#ddd}
.caption h3::after{content:"";position:absolute;left:0;bottom:-2px;width:100%;height:1px;background:rgba(255,255,255,.4)}
.book{position:absolute;right:8px;top:19px;border:1px solid var(--white);border-radius:8px;font-size:6.5px;padding:2px 8px}
.more{position:absolute;left:344px;top:530px;width:95px;height:24px;border:1px solid var(--white);border-radius:12px;text-align:center;line-height:22px;font-size:11px}

/* footer */
.footer{position:absolute;left:0;top:1010px;width:783px;height:190px;background:var(--footer)}
.footer .brand{left:58px;top:56px}
.col{position:absolute;top:38px}
.col h4{font-size:10px;font-weight:400;letter-spacing:.2px;margin-bottom:14px}
.col p{font-size:7.6px;line-height:14.5px;color:#eee}
.col.contact{left:224px}
.col.mail{left:419px}
.col.mail p{line-height:11px;width:140px}
.signup{display:flex;margin-top:9px}
.signup span{display:block;height:20px;font-size:7px;line-height:20px}
.signup .field{width:95px;background:var(--white);color:#999;padding-left:5px}
.signup .submit{width:37px;background:#555;color:#eee;text-align:center}
.col.follow{left:614px}
.social.foot{position:static;gap:9px}
.social.foot span{width:16px;height:16px;background:var(--white)}
.rule{position:absolute;left:49px;top:146px;width:668px;height:1px;background:#333}
.copyright{position:absolute;left:0;width:783px;top:164px;text-align:center;font-size:7.6px}
</style>
</head>
<body>
<div class="page">

  <header class="topbar">
    <div class="phone">
      <span class="phone-icon">
        <svg width="13" height="13" viewBox="0 0 24 24" fill="#fff"><path d="M6.6 10.8a15.1 15.1 0 0 0 6.6 6.6l2.2-2.2c.3-.3.7-.4 1-.2 1.1.4 2.3.6 3.6.6.6 0 1 .4 1 1V20c0 .6-.4 1-1 1C10.6 21 3 13.4 3 4c0-.6.4-1 1-1h3.5c.6 0 1 .4 1 1 0 1.3.2 2.5.6 3.6.1.3 0 .7-.2 1z"/></svg>
      </span>
      +852 5550 1742
    </div>
    <div class="brand">PASSMARLO</div>
    <div class="social top" aria-label="Social links"><span></span><span></span><span></span><span></span></div>
  </header>

  <nav class="nav">
    <a class="active" href="#">HOME</a>
    <a href="#">HOW TO ORDER</a>
    <a href="#">ABOUT US</a>
    <a href="#">CONTACT US</a>
    <a href="#">POLICIES</a>
    <a href="#">PRIVACY</a>
    <a href="#">CENTER SALE</a>
    <a href="#">ACCESS</a>
  </nav>

  <section class="hero" role="img" aria-label="Theatre stage with red velvet curtains and a wooden floor">
    <h1 class="hero-title">PASSMARLO</h1>
    <p class="hero-sub">quisquam est qui dolorem ipsum</p>
    <div class="hero-arrows">
      <span><svg width="8" height="8" viewBox="0 0 10 10"><path d="M6.5 1.5 3 5l3.5 3.5" stroke="#fff" stroke-width="1.4" fill="none"/></svg></span>
      <span><svg width="8" height="8" viewBox="0 0 10 10"><path d="M3.5 1.5 7 5 3.5 8.5" stroke="#fff" stroke-width="1.4" fill="none"/></svg></span>
    </div>
  </section>

  <section class="events">
    <h2>UPCOMING EVENTS</h2>

    <article class="event" style="left:58px;top:81px">
      <div class="photo" role="img" aria-label="Band playing guitar and drums on a lit stage" style="background:linear-gradient(160deg,#6a2a40,#2c1a3a 50%,#14131c)"></div>
      <div class="caption"><div class="date">1<br>NOV<br>2017</div><h3>NEQUE PORRO</h3><p>Dolorem ipsum quia dolor</p><span class="book">BOOK NOW</span></div>
    </article>
    <article class="event" style="left:284px;top:81px">
      <div class="photo" role="img" aria-label="Concert crowd with raised hands under warm stage lights" style="background:radial-gradient(ellipse at 50% 20%,#e08a3a,#7a3416 45%,#1c0e0a)"></div>
      <div class="caption"><div class="date">2<br>NOV<br>2017</div><h3>NEQUE PORRO</h3><p>Dolorem ipsum quia dolor</p><span class="book">BOOK NOW</span></div>
    </article>
    <article class="event" style="left:509px;top:81px">
      <div class="photo" role="img" aria-label="Close view of a guitarist playing on stage" style="background:linear-gradient(135deg,#9a5a86,#5a2e5a 50%,#2a1830)"></div>
      <div class="caption"><div class="date">2<br>NOV<br>2017</div><h3>NEQUE PORRO</h3><p>Dolorem ipsum quia dolor</p><span class="book">BOOK NOW</span></div>
    </article>

    <article class="event" style="left:58px;top:297px">
      <div class="photo" role="img" aria-label="Empty theatre hall with red seats and a curtain" style="background:linear-gradient(150deg,#a01830,#2a4a8a 40%,#3a5aa0 60%,#6a1624)"></div>
      <div class="caption"><div class="date">4<br>NOV<br>2017</div><h3>NEQUE PORRO</h3><p>Dolorem ipsum quia dolor</p><span class="book">BOOK NOW</span></div>
    </article>
    <article class="event" style="left:284px;top:297px">
      <div class="photo" role="img" aria-label="Juggler in a colourful jester costume" style="background:linear-gradient(160deg,#3a2a40,#7a3a7a 50%,#c04a70)"></div>
      <div class="caption"><div class="date">5<br>NOV<br>2017</div><h3>NEQUE PORRO</h3><p>Dolorem ipsum quia dolor</p><span class="book">BOOK NOW</span></div>
    </article>
    <article class="event" style="left:509px;top:297px">
      <div class="photo" role="img" aria-label="Rock band with guitars under blue stage lights" style="background:linear-gradient(150deg,#2a4a6a,#1a2a3e 50%,#0e141c)"></div>
      <div class="caption"><div class="date">6<br>NOV<br>2017</div><h3>NEQUE PORRO</h3><p>Dolorem ipsum quia dolor</p><span class="book">BOOK NOW</span></div>
    </article>

    <div class="more">VIEW MORE</div>
  </section>

  <footer class="footer">
    <div class="brand">PASSMARLO</div>
    <div class="col contact">
      <h4>CONTACT US</h4>
      <p>Address : 2710 Larkmoor Ave,<br>Dunhollow, Fl, 33140<br>Phone : 555-014-2290<br>Email : hello@passmarlo.com</p>
    </div>
    <div class="col mail">
      <h4>JOIN OUR MAILING LIST</h4>
      <p>Your about us information would fit here nicely.</p>
      <div class="signup"><span class="field">Email address</span><span class="submit">Submit</span></div>
    </div>
    <div class="col follow">
      <h4>FOLLOW US OUT THERE</h4>
      <div class="social foot" aria-label="Social links"><span></span><span></span><span></span><span></span></div>
    </div>
    <div class="rule"></div>
    <p class="copyright">Copyright © 2017. All Rights Reserved</p>
  </footer>

</div>
</body>
</html>
```